Bref créative
Business Cards for Young Professional
Professional, edgy, modern, credible, smart.
Professional
Doran Whitlake
Owner
4627 Mesa Lorna, NW
Albuquerque, NM 87309
dorenw@velbrik.example
velbrik.example
I plan to have cards printed on paper. But some will be made by metal etching. These metal cards will have a small area to be filled with melted brazing metal. I will attach pictures to demonstrate this principal.

```html
<!DOCTYPE html>
<html lang="en">
<head>
<meta charset="utf-8">
<title>Velbrik Consolidated – Business Card</title>
<link rel="stylesheet" href="https://fonts.googleapis.com/css2?family=Michroma&display=swap">
<style>
  :root {
    --page-bg: #e6e9ee;
    --card-white: #ffffff;
    --card-shade: #eef0f3;
    --brand-blue: #1d3a9c;
    --brand-blue-deep: #0c1f66;
    --steel-gray: #a9afb8;
    --ink-dark: #2b2f36;
    --ink-mid: #5b626c;
    --faint-mark: #e3e6ea;
  }
  * { box-sizing: border-box; margin: 0; padding: 0; }
  html, body {
    width: 1200px; height: 980px; overflow: hidden;
    background: var(--page-bg);
    font-family: "Michroma", sans-serif;
  }
  .canvas { position: relative; width: 1200px; height: 980px; }
  .card {
    position: absolute; left: 250px; width: 700px; height: 400px;
    border-radius: 22px; overflow: hidden;
    background: linear-gradient(160deg, var(--card-white), var(--card-shade));
    box-shadow: 0 10px 30px rgba(20, 30, 50, 0.18);
  }
  .card-front { top: 60px; }
  .card-back { top: 520px; }

  .front-art { position: absolute; inset: 0; }

  .brand {
    position: absolute; left: 42px; top: 54px;
    display: flex; align-items: center; gap: 12px;
  }
  .brand-dot {
    width: 40px; height: 40px; border-radius: 50%;
    background: var(--brand-blue); flex: none;
  }
  .brand-name {
    font-size: 15px; color: var(--brand-blue); letter-spacing: 0.3px;
    text-transform: uppercase; white-space: nowrap;
  }
  .brand-tagline {
    position: absolute; left: 94px; top: 92px;
    font-size: 7px; color: var(--steel-gray); letter-spacing: 5px;
    text-transform: uppercase; white-space: nowrap;
  }

  .contact-list {
    position: absolute; left: 42px; top: 150px;
    list-style: none;
  }
  .contact-item {
    display: flex; align-items: center; gap: 10px;
    font-size: 11px; color: var(--ink-dark); line-height: 1;
    margin-bottom: 11px; white-space: nowrap;
  }
  .contact-item.no-icon { padding-left: 26px; }
  .contact-icon { width: 16px; height: 16px; flex: none; }

  .owner {
    position: absolute; right: 44px; bottom: 34px; text-align: right;
  }
  .owner-name {
    font-size: 14px; color: var(--brand-blue-deep); letter-spacing: 1px;
  }
  .owner-role {
    margin-top: 6px; font-size: 9px; color: var(--ink-mid); letter-spacing: 1px;
  }

  .back-mark {
    position: absolute; right: 70px; top: 70px;
    width: 260px; height: 260px; border-radius: 50%;
    border: 34px solid var(--faint-mark);
  }
  .back-url {
    position: absolute; left: 48px; top: 60px;
    font-size: 13px; color: var(--ink-mid); letter-spacing: 9px;
    text-transform: uppercase; white-space: nowrap;
  }
</style>
</head>
<body>
<main class="canvas">

  <section class="card card-front" aria-label="Card front">
    <svg class="front-art" width="700" height="400" viewBox="0 0 700 400" aria-hidden="true">
      <defs>
        <linearGradient id="blueBand" x1="0" y1="0" x2="1" y2="1">
          <stop offset="0" stop-color="#2a4bb8"/>
          <stop offset="1" stop-color="#0c1f66"/>
        </linearGradient>
        <linearGradient id="steelBand" x1="0" y1="0" x2="1" y2="0">
          <stop offset="0" stop-color="#eef0f3"/>
          <stop offset="1" stop-color="#a9afb8"/>
        </linearGradient>
      </defs>
      <path d="M430 0 H700 V330 C590 318 490 220 430 0 Z" fill="url(#steelBand)"/>
      <path d="M458 0 H700 V312 C600 300 510 205 458 0 Z" fill="url(#blueBand)"/>
    </svg>

    <div class="brand">
      <span class="brand-dot"></span>
      <span class="brand-name">Velbrik Consolidated</span>
    </div>
    <div class="brand-tagline">Etched Metalworks</div>

    <ul class="contact-list">
      <li class="contact-item">
        <svg class="contact-icon" viewBox="0 0 16 16"><circle cx="8" cy="8" r="8" fill="#2b2f36"/><path d="M8 3.5a2.6 2.6 0 0 0-2.6 2.6C5.4 8.2 8 12 8 12s2.6-3.8 2.6-5.9A2.6 2.6 0 0 0 8 3.5z" fill="#fff"/><circle cx="8" cy="6.1" r="1" fill="#2b2f36"/></svg>
        4627 Mesa Lorna, NW
      </li>
      <li class="contact-item no-icon">Albuquerque, NM 87309</li>
      <li class="contact-item">
        <svg class="contact-icon" viewBox="0 0 16 16"><circle cx="8" cy="8" r="8" fill="#2b2f36"/><path d="M5.2 4.2l1.6-.3.8 2-1 .8a5.5 5.5 0 0 0 2.7 2.7l.8-1 2 .8-.3 1.6c-3.6.3-6.9-3-6.6-6.6z" fill="#fff"/></svg>
        505-555-0142
      </li>
      <li class="contact-item">
        <svg class="contact-icon" viewBox="0 0 16 16"><circle cx="8" cy="8" r="8" fill="#2b2f36"/><rect x="4" y="5.2" width="8" height="5.6" rx="0.6" fill="#fff"/><path d="M4.3 5.5L8 8.4l3.7-2.9" stroke="#2b2f36" stroke-width="0.8" fill="none"/></svg>
        dorenw@velbrik.example
      </li>
      <li class="contact-item">
        <svg class="contact-icon" viewBox="0 0 16 16"><circle cx="8" cy="8" r="8" fill="#2b2f36"/><circle cx="8" cy="8" r="4" fill="none" stroke="#fff" stroke-width="0.9"/><path d="M4 8h8M8 4c-1.6 2.2-1.6 5.8 0 8M8 4c1.6 2.2 1.6 5.8 0 8" stroke="#fff" stroke-width="0.7" fill="none"/></svg>
        www.velbrik.example
      </li>
    </ul>

    <div class="owner">
      <p class="owner-name">Doran Whitlake</p>
      <p class="owner-role">Owner</p>
    </div>
  </section>

  <section class="card card-back" aria-label="Card back">
    <div class="back-mark"></div>
    <p class="back-url">www.velbrik.example</p>
  </section>

</main>
</body>
</html>
```